Business card design for online Mandarin Learning School

We need a business card design for our online language learning school called "Maple Bridge Online for Mandarin Learning". Our existing website is https://www.maplebridgeonline.com
We have our logo already. We would like to see our business card design that can make our online teaching services to be innovative, young, energetic and fun to learn. Prefer to have a certain level of color matching with our website. Apart from "Maple Bridge Online", need to specifically state "for Mandarin Learning" as well on the business card.

```html
<!DOCTYPE html>
<html lang="en">
<head>
<meta charset="utf-8">
<title>Maple Bridge Online — Business Card</title>
<link rel="stylesheet" href="https://fonts.googleapis.com/css2?family=Cinzel:wght@400;600&family=Kalam:wght@400&family=EB+Garamond:wght@400&display=swap">
<style>
  :root {
    --teal: #1aa6b4;
    --teal-soft: #5fb7bd;
    --coral: #e35a59;
    --grey-text: #6f6f6f;
    --paper: #ffffff;
    --backdrop: #e9ecee;
  }
  * { box-sizing: border-box; margin: 0; padding: 0; }
  html, body {
    width: 1200px; height: 900px; overflow: hidden;
    background: var(--backdrop);
  }
  .canvas {
    position: relative; width: 1200px; height: 900px;
  }
  .card {
    position: absolute; left: 270px;
    width: 660px; height: 377px;
    border-radius: 26px;
    box-shadow: 0 8px 24px rgba(0,0,0,.18);
    overflow: hidden;
  }
  /* Front */
  .card--front {
    top: 48px;
    background: linear-gradient(35deg, var(--coral) 0%, #a87777 40%, #6a9a9f 65%, var(--teal) 100%);
    display: flex; flex-direction: column; align-items: center; justify-content: center;
    color: var(--paper);
  }
  .front-brand {
    display: flex; align-items: center; gap: 16px;
  }
  .front-brand__dot {
    width: 26px; height: 26px; border-radius: 50%; background: var(--paper);
  }
  .front-brand__name {
    font-family: "Cinzel", serif; font-weight: 400;
    font-size: 52px; letter-spacing: 2px;
  }
  .front-rule {
    width: 420px; height: 1.5px; background: var(--paper); margin: 14px 0 10px;
  }
  .front-url {
    font-family: "Cinzel", serif; font-size: 18px; letter-spacing: 2.5px;
  }
  /* Back */
  .card--back {
    top: 475px;
    background: var(--paper);
    display: flex; align-items: center;
    padding: 0 40px 0 52px;
  }
  .back-brand {
    width: 220px; display: flex; align-items: center; gap: 12px;
  }
  .back-brand__dot {
    width: 22px; height: 22px; border-radius: 50%; background: var(--coral); flex: none;
  }
  .back-brand__name {
    font-family: "Cinzel", serif; font-weight: 600;
    font-size: 22px; color: var(--teal); line-height: 1.15;
  }
  .back-divider {
    width: 1.5px; height: 120px; background: var(--teal); margin: 0 26px 0 20px;
  }
  .back-info { display: flex; flex-direction: column; }
  .back-title {
    font-family: "Cinzel", serif; font-size: 22px; color: var(--teal);
    letter-spacing: .5px;
  }
  .back-title .muted { color: var(--grey-text); }
  .back-tagline {
    font-family: "Kalam", cursive; font-size: 27px; color: var(--coral);
    line-height: 1.1; margin-bottom: 12px;
  }
  .back-web {
    font-family: "Cinzel", serif; font-size: 17px; color: var(--teal);
  }
  .back-web .muted { color: var(--grey-text); }
  .back-mail {
    font-family: "EB Garamond", serif; font-size: 18px; color: var(--teal);
  }
  .back-mail .muted { color: var(--grey-text); }
</style>
</head>
<body>
<main class="canvas">
  <section class="card card--front" aria-label="Card front">
    <div class="front-brand">
      <span class="front-brand__dot"></span>
      <span class="front-brand__name">Maple Bridge</span>
    </div>
    <div class="front-rule"></div>
    <p class="front-url">www.maplebridgeonline.com</p>
  </section>

  <section class="card card--back" aria-label="Card back">
    <div class="back-brand">
      <span class="back-brand__dot"></span>
      <span class="back-brand__name">Maple Bridge</span>
    </div>
    <div class="back-divider"></div>
    <div class="back-info">
      <p class="back-title">Maple <span class="muted">Bridge</span> Online for</p>
      <p class="back-tagline">Mandarin Learning</p>
      <p class="back-web"><span class="muted">www.</span>maplebridgeonline.com</p>
      <p class="back-mail"><span class="muted">support@</span>MapleBridgeOnline.com</p>
    </div>
  </section>
</main>
</body>
</html>
```